New Company Business Card Design

I have a new company logo and I want a new business card design. I dont know if the logo file i attached is in the correct format or quality. We are a New York City Specialty construction Firm specializing in high risk out of the box projects. I want a simple and classy business card that people will his card is as crisp as the work his company does.

Target Market(s)

Clients in the heavy construction industry in New York City

Industry/Entity Type

Construction Company

Contact Information for Business Card

Simple Classy - DIFFERENT

Font styles to use
Other font styles liked:
• Mach the logo font in some way

Colors

Designer to choose colors to be used in the design.

Requirements
Must have
• Uniqueness
Nice to have
• Nothing particular - Just different and classy - Timeless
Should not have
• Goofy Shit or Gimmicky shit

```html
<!DOCTYPE html>
<html lang="en">
<head>
<meta charset="utf-8">
<title>Kestrel Vane Builders – Business Card</title>
<link href="https://fonts.googleapis.com/css2?family=Open+Sans:wght@400;600&display=swap" rel="stylesheet">
<style>
  :root {
    --backdrop: #2a2a2c;
    --card: #1b1b1d;
    --card-edge: #262628;
    --blue: #3d8ed3;
    --blue-soft: #5b9fd6;
    --text-light: #d9dadc;
    --text-muted: #b8babd;
  }
  * { margin: 0; padding: 0; box-sizing: border-box; }
  html, body {
    width: 1200px;
    height: 942px;
    overflow: hidden;
    background: var(--backdrop);
    font-family: "Open Sans", Arial, sans-serif;
  }
  .sheet {
    width: 1200px;
    height: 942px;
    display: flex;
    flex-direction: column;
    align-items: center;
    justify-content: center;
    gap: 44px;
  }
  .card {
    position: relative;
    width: 700px;
    height: 400px;
    background: var(--card);
    border: 1px solid var(--card-edge);
    border-radius: 26px;
    box-shadow: 0 14px 30px rgba(0,0,0,0.45);
  }

  /* Front */
  .card--front .brand {
    position: absolute;
    left: 0; right: 0;
    top: 150px;
    text-align: center;
    color: var(--blue);
    font-weight: 600;
    font-size: 40px;
    letter-spacing: 3px;
  }
  .card--front .website {
    position: absolute;
    left: 0; right: 0;
    top: 262px;
    text-align: center;
    color: var(--blue);
    font-size: 15px;
    letter-spacing: 3px;
  }

  /* Back */
  .card--back .brand {
    position: absolute;
    left: 60px;
    top: 58px;
    color: var(--blue);
    font-weight: 600;
    font-size: 26px;
    letter-spacing: 2px;
  }
  .card--back .identity {
    position: absolute;
    left: 300px;
    top: 170px;
  }
  .identity .name {
    color: var(--text-light);
    font-size: 24px;
    letter-spacing: 1px;
  }
  .identity .role {
    color: var(--blue-soft);
    font-size: 15px;
    margin-top: 4px;
  }
  .contacts {
    list-style: none;
    margin-top: 22px;
  }
  .contacts li {
    display: flex;
    align-items: center;
    gap: 12px;
    color: var(--text-muted);
    font-size: 15px;
    line-height: 30px;
  }
  .contacts svg { width: 14px; height: 14px; flex: none; }
</style>
</head>
<body>
  <main class="sheet">
    <section class="card card--front" aria-label="Card front">
      <div class="brand">KESTREL VANE BUILDERS, INC.</div>
      <div class="website">www.yourwebsite.com</div>
    </section>

    <section class="card card--back" aria-label="Card back">
      <div class="brand">KESTREL VANE BUILDERS, INC.</div>
      <div class="identity">
        <div class="name">YOUR NAME</div>
        <div class="role">Job Title</div>
        <ul class="contacts">
          <li>
            <svg viewBox="0 0 14 14" aria-hidden="true"><rect x="3.5" y="1" width="7" height="12" rx="1.5" fill="none" stroke="#9fc6ea" stroke-width="1.4"/></svg>
            000 000 0000
          </li>
          <li>
            <svg viewBox="0 0 14 14" aria-hidden="true"><rect x="1" y="3" width="12" height="8" fill="none" stroke="#9fc6ea" stroke-width="1.4"/><path d="M1 3 L7 8 L13 3" fill="none" stroke="#9fc6ea" stroke-width="1.4"/></svg>
            youremail@xyz.com
          </li>
          <li>
            <svg viewBox="0 0 14 14" aria-hidden="true"><circle cx="7" cy="7" r="5.8" fill="none" stroke="#9fc6ea" stroke-width="1.2"/><ellipse cx="7" cy="7" rx="2.5" ry="5.8" fill="none" stroke="#9fc6ea" stroke-width="1"/><line x1="1.2" y1="7" x2="12.8" y2="7" stroke="#9fc6ea" stroke-width="1"/></svg>
            www.yourwebsite.com
          </li>
        </ul>
      </div>
    </section>
  </main>
</body>
</html>
```